MD Business Card

I want to create a simple business card.
I am a consultant. I design and develop furniture, lighting and accessories for hospitality and retail brands.
I want the card to be simple and clean. Not too much of a logo - but it needs the basic information shown on the attached file.
Also - I have shown some fonts that I like on the attached file.
The card can be square or rectangle. It should be double sided.
I prefer 1-2 colors (not too colorful - but using color an an accent) Even if using color on the edges as an accent.

My snapquilt link shows some other graphics styles that I like. I like clean and simple.
http://www.snapquilt.com/marendowsett/business-cards/

Reason: I needed a few more days to see some of the options evolve.

Hospitality

```html
<!DOCTYPE html>
<html lang="en">
<head>
<meta charset="utf-8">
<title>MD Business Card — Front and Back</title>
<link rel="stylesheet" href="https://fonts.googleapis.com/css2?family=Mulish:wght@300;400;700&display=swap">
<style>
  :root {
    --backdrop: #3a383c;
    --card: #ffffff;
    --band: #a7a7a7;
    --band-edge: #c9c9c9;
    --ink: #333333;
    --ink-soft: #6f6f6f;
    --label: #d6d6d6;
  }
  * { margin: 0; padding: 0; box-sizing: border-box; }
  html, body { width: 1200px; height: 1000px; overflow: hidden; }
  body {
    background: var(--backdrop);
    font-family: "Mulish", "Helvetica Neue", Arial, sans-serif;
    position: relative;
  }
  .card {
    position: absolute;
    width: 423px;
    height: 723px;
    background: var(--card);
  }
  .card--front { left: 125px; top: 126px; }
  .card--back { left: 682px; top: 145px; }

  .contact-band {
    position: absolute;
    left: 163px;
    top: 0;
    width: 96px;
    height: 511px;
    background: var(--band);
    border: 3px solid var(--band-edge);
    border-top: none;
    outline: 1px solid #9a9a9a;
    outline-offset: -5px;
    display: flex;
    justify-content: center;
    align-items: flex-end;
    padding-bottom: 18px;
  }
  .contact-band__text {
    writing-mode: vertical-rl;
    color: #ffffff;
    font-size: 19px;
    font-weight: 400;
    line-height: 30px;
    text-align: end;
  }
  .owner-name {
    position: absolute;
    left: 0;
    width: 100%;
    top: 543px;
    text-align: center;
    color: var(--ink);
  }
  .owner-name__first {
    display: block;
    font-size: 31px;
    font-weight: 300;
    letter-spacing: 3px;
    line-height: 36px;
  }
  .owner-name__last {
    display: block;
    font-size: 44px;
    font-weight: 700;
    letter-spacing: 1.5px;
    line-height: 50px;
  }

  .services {
    position: absolute;
    inset: 0;
    display: flex;
    justify-content: center;
    align-items: center;
  }
  .services__block {
    writing-mode: vertical-rl;
    text-align: center;
  }
  .services__title {
    display: block;
    font-size: 29px;
    font-weight: 400;
    color: var(--ink);
    line-height: 46px;
    letter-spacing: 0.5px;
  }
  .services__list {
    display: block;
    font-size: 24px;
    font-weight: 400;
    color: var(--ink-soft);
    letter-spacing: 2.5px;
    line-height: 34px;
  }
  .side-label {
    position: absolute;
    color: var(--label);
    font-size: 20px;
    font-weight: 400;
    transform: translateX(-50%);
  }
  .side-label--front { left: 245px; top: 910px; }
  .side-label--back { left: 945px; top: 912px; }
</style>
</head>
<body>
  <section class="card card--front" aria-label="Card front">
    <div class="contact-band">
      <p class="contact-band__text">maren@marendowsett.com<br>917.555.0148</p>
    </div>
    <h1 class="owner-name">
      <span class="owner-name__first">MAREN</span>
      <span class="owner-name__last">DOWSETT</span>
    </h1>
  </section>

  <section class="card card--back" aria-label="Card back">
    <div class="services">
      <p class="services__block">
        <span class="services__title">Design &amp; Development:</span>
        <span class="services__list">furniture &bull; fixtures &bull; lighting &bull; textiles etc.</span>
      </p>
    </div>
  </section>

  <p class="side-label side-label--front">Front</p>
  <p class="side-label side-label--back">Back</p>
</body>
</html>
```